Modern Minimalistic Supplement Label

Opportunity for recurring projects with a growing company. We have provided a detailed creative brief and all necessary files and guidelines. If you have any questions we will be closely monitoring the discussion board and email provided.

THE NAMES LISTED IN THE BRIEF ARE DIFFERENT FROM THE LABEL TEMPLATES. This is a private label brand. The label templates given are generic so please examine the entire brief before starting.

Use the PSD mockups attached and pair the labels with the correct bottles.

Do not use an entirely white background.

This could be excellent portfolio material.

Start by looking at the "CREATIVE_BRIEF" file. Logo files are contained in the "58213907" zip file.

UPDATE* Use the following business address for the "manufactured for" box on the labels.

Fernwick
4817 Larkmoor Ave. #2209
Ann Arbor MI 48196

Target Market(s)

All information provided in "CREATIVE_BRIEF" file.

Industry/Entity Type

Supplement

Requirements
Must have
• All information provided in "CREATIVE_BRIEF" file.
Nice to have
Should not have

```html
<!DOCTYPE html>
<html lang="en">
<head>
<meta charset="utf-8">
<title>Fernwick Whey Protein Isolate Blend – Chocolate Label</title>
<link href="https://fonts.googleapis.com/css2?family=Bebas+Neue&family=Barlow+Semi+Condensed:wght@400&family=Open+Sans:wght@400;700;800&family=Raleway:wght@400;700&family=Roboto:wght@300;400&display=swap" rel="stylesheet">
<style>
  :root{
    --backdrop:#ebebeb;
    --band:#8a4516;
    --label-black:#050505;
    --mountain:#232323;
    --headline:#95511f;
    --band-text:#f2d6bb;
    --white:#ffffff;
    --rule:#555555;
    --ink:#111111;
  }
  *{margin:0;padding:0;box-sizing:border-box}
  html,body{width:1200px;height:1001px;overflow:hidden;background:var(--backdrop)}
  body{font-family:"Open Sans",Arial,sans-serif}
  .canvas{position:relative;width:1200px;height:1001px;overflow:hidden}

  .label{
    position:absolute;left:20px;top:270px;width:1828px;height:725px;overflow:hidden;
    transform:scale(0.6346);transform-origin:0 0;
    background:var(--label-black);color:var(--white);
    box-shadow:0 18px 30px rgba(0,0,0,.25);
  }
  .overlap-strip{position:absolute;left:0;top:0;width:60px;height:725px;background:var(--white)}
  .band{position:absolute;left:60px;width:1768px;height:70px;background:var(--band)}
  .band--top{top:0}
  .band--bottom{top:655px;display:flex;align-items:center;justify-content:center;
    font-size:26px;font-weight:400;color:var(--band-text);letter-spacing:.3px}
  .backdrop-art{position:absolute;left:440px;top:170px;width:1388px;height:485px;
    background:linear-gradient(180deg,rgba(40,40,40,0) 0%,rgba(38,38,38,.8) 35%,var(--mountain) 100%);
    clip-path:polygon(0 100%,35% 40%,55% 55%,87% 0,100% 20%,100% 100%)}

  .center{position:absolute;left:560px;width:800px;text-align:center}
  .brand-name{font-weight:700;letter-spacing:6px;line-height:1}
  .center.brand-name{top:182px;font-size:46px}
  .product-name{top:232px;font-family:"Bebas Neue",sans-serif;font-weight:400;font-size:124px;line-height:1;color:var(--headline);letter-spacing:1px}
  .product-type{top:346px;font-family:"Barlow Semi Condensed",sans-serif;font-size:52px;font-weight:400;line-height:1;letter-spacing:1px}
  .divider{position:absolute;left:664px;width:593px;height:1px;background:var(--rule)}
  .flavor{top:446px;font-size:38px;font-weight:800;letter-spacing:5px;line-height:1}
  .protein-claim{top:518px;font-family:"Barlow Semi Condensed",sans-serif;font-size:35px;line-height:38px}
  .benefit{top:609px;font-family:"Barlow Semi Condensed",sans-serif;font-size:27px;letter-spacing:.5px}

  .left-panel{position:absolute;left:75px;top:0;width:347px;font-family:"Raleway",Arial,sans-serif}
  .left-panel .brand-name{position:absolute;top:158px;width:347px;text-align:center;font-family:"Open Sans",Arial,sans-serif;font-size:30px;letter-spacing:4px}
  .use-title{position:absolute;top:214px;width:347px;text-align:center;font-size:12.5px;font-weight:700}
  .use-text{position:absolute;top:230px;width:347px;font-size:12px;line-height:16px}

  .amino-box{position:absolute;top:296px;width:347px;height:217px;border:1.5px solid var(--white);border-radius:3px}
  .amino-head{height:40px;border-bottom:1.5px solid var(--white);text-align:center;font-size:12px;font-weight:700;line-height:14.5px;padding-top:5px}
  .amino-cols{display:flex;padding:7px 10px 0 12px;height:146px;border-bottom:1px solid #888}
  .amino-col{flex:1;font-size:12px;line-height:14.7px}
  .amino-col + .amino-col{border-left:1.5px dashed #bbb;padding-left:18px}
  .amino-row{display:flex;white-space:nowrap}
  .amino-row span:first-child{width:93px}
  .amino-total{display:flex;font-size:12px;padding:6px 12px}
  .amino-total span:first-child{width:93px}

  .fda-box{position:absolute;top:540px;width:347px;height:64px;border:1.5px solid var(--white);border-radius:3px;
    font-size:11.5px;font-weight:700;line-height:15px;padding:6px 10px}

  .facts{position:absolute;left:1522px;top:27px;width:284px;height:440px;overflow:hidden;background:var(--white);color:var(--ink);
    border:1px solid #999;padding:0 3px;font-family:"Roboto",Arial,sans-serif;font-size:12px}
  .facts-title{font-size:34px;font-weight:300;line-height:38px;white-space:nowrap}
  .facts-serving{font-size:16.5px;font-weight:300;line-height:21px;white-space:nowrap}
  .bar-thick{height:7px;background:var(--ink);margin:2px 0 1px}
  .bar-mid{height:3px;background:var(--ink);margin:1px 0 0}
  .facts-header{display:flex;justify-content:space-between;font-size:9.5px;height:14px;align-items:center;padding-right:12px}
  .fact-row{display:grid;grid-template-columns:1fr 62px 54px;height:17.5px;align-items:center;border-bottom:1px solid #999;font-weight:300;white-space:nowrap}
  .fact-row span:nth-child(2),.fact-row span:nth-child(3){text-align:right}
  .fact-row.indent span:first-child{padding-left:7px}
  .fact-row.indent2 span:first-child{padding-left:14px}
  .fact-row.plain{border-bottom:0}
  .blend{display:grid;grid-template-columns:1fr 62px 54px;font-weight:300;line-height:15px;white-space:nowrap}
  .blend span:nth-child(2),.blend span:nth-child(3){text-align:right}
  .blend .sub{grid-column:1 / 4;padding-left:7px;letter-spacing:-.1px}
  .blend + .blend{border-top:1px solid #999;padding-top:3px;margin-top:2px}
  .footnote{font-size:9.5px;line-height:12px;font-weight:300;padding-top:2px;white-space:nowrap}

  .ingredients{position:absolute;left:1525px;top:476px;width:290px;font-family:"Roboto",Arial,sans-serif;font-size:10px;line-height:12.5px;font-weight:300}
  .made-for{position:absolute;left:1525px;top:542px;font-family:"Roboto",Arial,sans-serif;font-size:12.5px;font-weight:400}
  .made-for-brand{position:absolute;left:1522px;top:575px;font-size:15px;font-weight:700;letter-spacing:2px}
  .made-for-address{position:absolute;left:1522px;top:593px;font-family:"Roboto",Arial,sans-serif;font-size:12.5px;line-height:15px;font-weight:300;font-style:normal}
</style>
</head>
<body>
<div class="canvas">
<div class="label">
  <div class="overlap-strip"></div>
  <div class="band band--top"></div>
  <div class="backdrop-art" role="img" aria-label="Faint mountain range backdrop"></div>

  <section class="left-panel">
    <div class="brand-name">FERNWICK</div>
    <div class="use-title">SUGGESTED USE:</div>
    <p class="use-text">Mix one rounded scoop with 4-6oz of water, milk, or your favorite beverage. Vary the amount of liquid for taste preference.</p>

    <div class="amino-box">
      <div class="amino-head">APPROXIMATE AMINO ACIDS PER SERVING<br>(NATURALLY OCCURRING)</div>
      <div class="amino-cols">
        <div class="amino-col">
          <div class="amino-row"><span>Alanine</span><span>1208 mg</span></div>
          <div class="amino-row"><span>Aspartic Acid</span><span>2515 mg</span></div>
          <div class="amino-row"><span>Glutamic Acid</span><span>4015 mg</span></div>
          <div class="amino-row"><span>Histidine</span><span>422 mg</span></div>
          <div class="amino-row"><span>Leucine*</span><span>2436 mg</span></div>
          <div class="amino-row"><span>Methionine</span><span>528 mg</span></div>
          <div class="amino-row"><span>Proline</span><span>1416 mg</span></div>
          <div class="amino-row"><span>Threonine</span><span>1618 mg</span></div>
          <div class="amino-row"><span>Tyrosine</span><span>727 mg</span></div>
        </div>
        <div class="amino-col">
          <div class="amino-row"><span>Arginine</span><span>665 mg</span></div>
          <div class="amino-row"><span>Cystine</span><span>566 mg</span></div>
          <div class="amino-row"><span>Glycine</span><span>437 mg</span></div>
          <div class="amino-row"><span>Isoleucine*</span><span>1422 mg</span></div>
          <div class="amino-row"><span>Lysine</span><span>2389 mg</span></div>
          <div class="amino-row"><span>Phenylalanine</span><span>756 mg</span></div>
          <div class="amino-row"><span>Serine</span><span>1231 mg</span></div>
          <div class="amino-row"><span>Tryptophan</span><span>416 mg</span></div>
          <div class="amino-row"><span>Valine*</span><span>1260 mg</span></div>
        </div>
      </div>
      <div class="amino-total"><span>Total BCAAs</span><span>5147 mg</span></div>
    </div>

    <div class="fda-box">* These statements have not been evaluated by the Food and Drug Administration. This product is not intended to diagnose, treat, cure or prevent any disease.</div>
  </section>

  <div class="center brand-name">FERNWICK</div>
  <h1 class="center product-name">WHEY PROTEIN</h1>
  <div class="center product-type">ISOLATE BLEND</div>
  <div class="divider" style="top:431px"></div>
  <div class="center flavor">CHOCOLATE</div>
  <div class="divider" style="top:499px"></div>
  <div class="center protein-claim">24G<br>PROTEIN</div>
  <div class="center benefit">FOR INCREASED MUSCULAR RECOVERY</div>

  <section class="facts">
    <div class="facts-title">Supplement Facts</div>
    <div class="facts-serving">Serving Size 32g (1 Rounded Scoop)</div>
    <div class="facts-serving">Servings Per Container&nbsp; 28</div>
    <div class="bar-thick"></div>
    <div class="facts-header"><span>Amount Per Serving</span><span>% Daily Value**</span></div>
    <div class="bar-mid"></div>
    <div class="fact-row"><span>Calories&nbsp; 120</span><span></span><span></span></div>
    <div class="fact-row"><span>Total Fat</span><span>2 g</span><span>3%</span></div>
    <div class="fact-row indent"><span>Saturated Fat</span><span>1 g</span><span>7%</span></div>
    <div class="fact-row"><span>Cholesterol</span><span>60 mg</span><span>20%</span></div>
    <div class="fact-row"><span>Total Carbohydrate</span><span>4 g</span><span>1%</span></div>
    <div class="fact-row indent"><span>Dietary Fiber</span><span>&lt; 1 g</span><span>2%</span></div>
    <div class="fact-row indent"><span>Total Sugars</span><span>2 g</span><span></span></div>
    <div class="fact-row indent2"><span>Includes 0g Added Sugars</span><span>0%</span><span></span></div>
    <div class="fact-row"><span>Protein</span><span>24 g</span><span>48%</span></div>
    <div class="fact-row"><span>Calcium</span><span>125 mg</span><span>10%</span></div>
    <div class="fact-row"><span>Sodium</span><span>50 mg</span><span>2%</span></div>
    <div class="fact-row"><span>Iron</span><span>1 mg</span><span>4%</span></div>
    <div class="fact-row plain"><span>Potassium</span><span>290 mg</span><span>6%</span></div>
    <div class="bar-mid"></div>
    <div class="blend"><span>Whey Protein Blend</span><span>29 g</span><span>‡</span><span class="sub">(Whey Protein Concentrate, Whey Protein Isolate.)</span></div>
    <div class="blend"><span>Digestive Enzyme Blend</span><span>10 mg</span><span>‡</span><span class="sub">(Papain, Protease)</span></div>
    <div class="bar-thick" style="height:5px"></div>
    <div class="footnote">**Percent Daily Values are based on a 2,000 calorie diet.<br>‡Daily Value not established.</div>
  </section>

  <p class="ingredients">Other Ingredients: Cocoa (processed with alkali), Natural Flavors, Stevia.<br>Contains: Milk, Soy.</p>
  <div class="made-for">Manufactured for:</div>
  <div class="made-for-brand">FERNWICK</div>
  <address class="made-for-address">Fernwick, 4817 Larkmoor Ave. #2209<br>Ann Arbor MI 48196</address>

  <div class="band band--bottom">NET WT. 907 G (2 LB) | DIETARY SUPPLEMENT</div>
</div>
</div>
</body>
</html>
```